design a construction company business card

Design business card around our logo. Card must have all the typical info: name, title, address, phone, email, business name, etc. Somewhere on the card I would like to see our motto "Built on integrity... Inspired by commitment." Consider adding a splash of bright orange to the card to complement the blues and silvers/grays in the logo. We are open to metallic inks, textures, etc. We would like to see options on both light and dark backgrounds. The font in the logo is Euro Technic Extended Regular.

```html
<!DOCTYPE html>
<html lang="en">
<head>
<meta charset="utf-8">
<title>Halden Contracting – Business Card</title>
<link rel="stylesheet" href="https://fonts.googleapis.com/css2?family=Open+Sans:wght@400;600;700&display=swap">
<style>
  :root {
    --page-bg: #2a2d31;
    --card-bg: #1d1c1e;
    --card-edge: #111012;
    --brand-blue: #2f6fd6;
    --text-white: #f2f2f2;
    --text-muted: #bdbdbd;
    --rule-white: #e9e9e9;
  }
  * { margin: 0; padding: 0; box-sizing: border-box; }
  html, body {
    width: 1200px;
    height: 900px;
    overflow: hidden;
    background: var(--page-bg);
    font-family: "Open Sans", Arial, sans-serif;
  }
  .sheet {
    width: 1200px;
    height: 900px;
    display: flex;
    flex-direction: column;
    align-items: center;
    justify-content: center;
    gap: 56px;
  }
  .card {
    position: relative;
    width: 630px;
    height: 360px;
    background: var(--card-bg);
    border-radius: 4px;
    box-shadow: 0 2px 0 var(--card-edge), 0 14px 30px rgba(0,0,0,0.45);
    overflow: hidden;
  }

  /* Logo side */
  .card--logo {
    display: flex;
    align-items: center;
    justify-content: center;
  }
  .brand {
    display: flex;
    align-items: center;
    gap: 12px;
    color: var(--brand-blue);
    font-weight: 700;
  }
  .brand__mark {
    width: 14px;
    height: 14px;
    background: var(--brand-blue);
  }
  .brand__name {
    font-size: 30px;
    letter-spacing: 1px;
    line-height: 1;
  }
  .brand--small .brand__name { font-size: 18px; }
  .brand--small .brand__mark { width: 10px; height: 10px; }

  /* Info side */
  .person {
    position: absolute;
    left: 62px;
    top: 62px;
    color: var(--text-white);
  }
  .person__name {
    font-size: 19px;
    font-weight: 600;
    line-height: 1.2;
  }
  .person__title {
    font-size: 11px;
    color: var(--text-muted);
    margin-top: 2px;
  }
  .contact {
    position: absolute;
    left: 50px;
    top: 152px;
    list-style: none;
    color: var(--text-white);
    font-size: 13px;
    line-height: 1.8;
  }
  .card__brand {
    position: absolute;
    right: 44px;
    top: 140px;
  }
  .address {
    position: absolute;
    right: 70px;
    top: 210px;
    color: var(--text-white);
    font-size: 15px;
  }
  .rule {
    position: absolute;
    left: 48px;
    right: 92px;
    top: 262px;
    height: 2px;
    background: var(--rule-white);
  }
  .motto {
    position: absolute;
    left: 52px;
    top: 276px;
    color: var(--brand-blue);
    font-size: 15px;
    letter-spacing: 1.2px;
  }
</style>
</head>
<body>
<main class="sheet">
  <section class="card card--logo" aria-label="Card back">
    <div class="brand">
      <span class="brand__mark"></span>
      <span class="brand__name">Halden Contracting, Inc.</span>
    </div>
  </section>

  <section class="card card--info" aria-label="Card front">
    <div class="person">
      <p class="person__name">Your Name</p>
      <p class="person__title">Title</p>
    </div>
    <ul class="contact">
      <li>+99 999 9999</li>
      <li>youremail@website.com</li>
    </ul>
    <div class="brand brand--small card__brand">
      <span class="brand__mark"></span>
      <span class="brand__name">Halden Contracting, Inc.</span>
    </div>
    <p class="address">Address location</p>
    <div class="rule"></div>
    <p class="motto">Built on integrity... Inspired by commitment.</p>
  </section>
</main>
</body>
</html>
```